Pellmark Ridgeway LLC stationery, business card and web page design.

i need a full set of stationery designed using the name "Pellmark Ridgeway LLC" with a tag line "construction consulting services". using the uploaded monkey icon as the logo.

i like the colors orange, green and black in general but im not limited to that. the company offers consulting services to various types of construction businesses.

i travel around the country in a 4x4 camper offering consulting services and technical training short term and long to various types of construction companies.

Construction Company

Peter Lund
p.lund@pellmarkridgeway.example
2748 Fenwick Rd
Maple Glen, NY 10943
555 014 3627

list these services on the card.

Business Consulting
Capital Investments
Marketing Implementations
Technical Training

1 page

Designer to choose colors to be used in the design.

• company info and use of the monkey icon i provided.
• a fun but professional design
• the color red

```html
<!DOCTYPE html>
<html lang="en">
<head>
<meta charset="utf-8">
<title>Pellmark Ridgeway LLC — Stationery Set</title>
<link href="https://fonts.googleapis.com/css2?family=Oswald:wght@400&family=Jost:wght@400;500&display=swap" rel="stylesheet">
<style>
  :root {
    --orange: #e85f33;
    --orange-deep: #cf5530;
    --black: #0d0d0d;
    --white: #ffffff;
    --paper-ground: #e9e6e2;
    --ink: #3a3a3a;
    --ink-soft: #6f6f6f;
    --faint-mark: #ece9e6;
    --shadow: 0 2px 5px rgba(0,0,0,0.14);
  }
  * { margin: 0; padding: 0; box-sizing: border-box; }
  html, body { width: 1200px; height: 835px; overflow: hidden; }
  body {
    background: var(--paper-ground);
    font-family: "Jost", "Futura", sans-serif;
    color: var(--ink);
    position: relative;
  }
  address { font-style: normal; }
  .piece { position: absolute; box-shadow: var(--shadow); overflow: hidden; }
  .brand-name {
    font-family: "Oswald", "Arial Narrow", sans-serif;
    font-weight: 400;
    letter-spacing: 0.06em;
    text-transform: uppercase;
    white-space: nowrap;
  }
  .tagline { font-family: "Jost", "Futura", sans-serif; font-weight: 400; letter-spacing: 0.08em; text-transform: uppercase; white-space: nowrap; }
  .mark-dot { position: absolute; border-radius: 50%; background: var(--black); }
  .faint-mark { position: absolute; border-radius: 50%; }
  .icon { width: 5px; height: 5px; display: inline-block; vertical-align: middle; }

  /* Letterhead */
  .letterhead { left: 76px; top: 63px; width: 358px; height: 460px; background: var(--white); }
  .letterhead .side-band { position: absolute; left: 0; top: 0; width: 16px; height: 100%; background: var(--orange); }
  .letterhead .mark-dot { left: 55px; top: 14px; width: 36px; height: 36px; }
  .letterhead .brand-name { position: absolute; left: 32px; top: 56px; font-size: 8px; color: var(--orange); }
  .letterhead .tagline { position: absolute; left: 32px; top: 69px; font-size: 4.4px; color: var(--ink-soft); }
  .letterhead .sender { position: absolute; right: 29px; top: 16px; text-align: right; font-size: 6.4px; line-height: 9px; color: var(--ink); }
  .letterhead .sender .gap { height: 4px; }
  .letterhead .sender .icon { margin-left: 4px; color: var(--orange); }
  .letterhead .greeting { position: absolute; left: 32px; top: 98px; font-size: 8px; color: var(--ink); }
  .letterhead .body-copy { position: absolute; left: 32px; top: 114px; width: 297px; font-size: 5px; line-height: 7px; color: var(--ink-soft); }
  .letterhead .body-copy p { margin-bottom: 5px; }
  .letterhead .body-copy p.spaced { margin-top: 11px; }
  .letterhead .closing { position: absolute; left: 50px; top: 341px; font-size: 7.5px; color: var(--ink); }
  .letterhead .signer { position: absolute; left: 52px; top: 353px; font-size: 4.8px; color: var(--ink-soft); }
  .letterhead .sign-rule { position: absolute; left: 34px; top: 364px; width: 64px; height: 1px; background: var(--ink); }
  .letterhead .signature { position: absolute; left: 36px; top: 370px; width: 52px; height: 26px; background: #e4e4e4; border-radius: 2px; }
  .letterhead .faint-mark { left: 226px; top: 340px; width: 106px; height: 106px; background: var(--faint-mark); }

  /* Folder */
  .folder { left: 464px; top: 63px; width: 356px; height: 460px; background: var(--orange); }
  .folder .faint-mark { left: 98px; top: 150px; width: 160px; height: 160px; background: var(--orange-deep); }

  /* Business card front */
  .card-front { left: 846px; top: 73px; width: 282px; height: 162px; background: var(--white); }
  .card-front .side-band { position: absolute; left: 0; top: 0; width: 10px; height: 100%; background: var(--orange); }
  .card-front .mark-dot { left: 20px; top: 14px; width: 44px; height: 44px; }
  .card-front .brand-name { position: absolute; right: 14px; top: 26px; font-size: 15px; color: var(--orange); letter-spacing: 0.08em; }
  .card-front .tagline { position: absolute; right: 14px; top: 48px; font-size: 5px; color: var(--ink-soft); }
  .card-front .services { position: absolute; right: 14px; top: 60px; list-style: none; text-align: right; font-size: 5.2px; line-height: 7.5px; color: var(--black); }
  .card-front .services li { display: inline; }
  .card-front .services li + li::before { content: "•"; color: var(--orange); margin: 0 3px; }
  .card-front .person { position: absolute; right: 14px; top: 87px; font-size: 12.5px; color: var(--orange); letter-spacing: 0.03em; }
  .card-front .role { position: absolute; right: 14px; top: 105px; font-size: 5.6px; color: var(--black); }
  .card-front .rule { position: absolute; left: 20px; right: 14px; top: 116px; height: 1px; background: var(--orange); }
  .card-front .contacts { position: absolute; left: 20px; top: 124px; font-size: 6.2px; line-height: 9px; color: var(--black); }
  .card-front .contacts .icon { margin-right: 4px; color: var(--orange); }
  .card-front .address { position: absolute; right: 14px; top: 133px; text-align: right; font-size: 6.2px; line-height: 9px; color: var(--black); }

  /* Business card backs */
  .card-back { left: 846px; width: 282px; height: 161px; }
  .card-back.is-orange { top: 342px; background: var(--orange); }
  .card-back.is-black { top: 610px; background: var(--black); }
  .card-back .faint-mark { left: 91px; top: 32px; width: 100px; height: 100px; }
  .card-back.is-orange .faint-mark { background: var(--orange-deep); }
  .card-back.is-black .faint-mark { background: #2a1d17; }
  .card-back .brand-name { position: absolute; left: 0; right: 0; top: 70px; text-align: center; font-size: 13.5px; color: var(--white); }
  .card-back .web { position: absolute; left: 0; right: 0; bottom: 12px; text-align: center; font-size: 6px; color: var(--white); letter-spacing: 0.03em; }

  /* Envelope with flap */
  .envelope { left: 81px; top: 545px; width: 361px; height: 225px; background: var(--white); border-radius: 40px 40px 0 0; }
  .envelope .flap { position: absolute; left: 0; top: 0; width: 100%; height: 34px; background: var(--orange); }
  .envelope .mark-dot { left: 170px; top: 5px; width: 24px; height: 24px; }
  .envelope .brand-name { position: absolute; left: 0; right: 0; top: 118px; text-align: center; font-size: 19px; color: var(--black); }

  /* DL envelope */
  .dl-envelope { left: 461px; top: 574px; width: 365px; height: 201px; background: var(--orange); }
  .dl-envelope .side-band { position: absolute; left: 0; top: 0; width: 13px; height: 100%; background: var(--black); }
  .dl-envelope .faint-mark { left: 128px; top: 40px; width: 130px; height: 130px; background: var(--orange-deep); }
  .dl-envelope .brand-name { position: absolute; left: 13px; right: 0; top: 86px; text-align: center; font-size: 18px; color: var(--white); }
  .dl-envelope .contacts { position: absolute; left: 29px; top: 167px; font-size: 5.3px; line-height: 8px; color: var(--white); }
  .dl-envelope .contacts .icon { margin-right: 3px; color: var(--white); }
  .dl-envelope .address { position: absolute; right: 15px; top: 175px; text-align: right; font-size: 5.3px; line-height: 8px; color: var(--white); }
</style>
</head>
<body>

<svg width="0" height="0" style="position:absolute">
  <defs>
    <symbol id="icon-phone" viewBox="0 0 10 10"><path d="M2 1 L4 1 L4.6 3.2 L3.4 4 Q4.4 6 6 6.6 L6.8 5.4 L9 6 L9 8 Q9 9 8 9 Q1 8.4 1 2 Q1 1 2 1 Z" fill="currentColor"/></symbol>
    <symbol id="icon-mail" viewBox="0 0 10 10"><rect x="1" y="2.5" width="8" height="5.5" fill="none" stroke="currentColor" stroke-width="1.1"/><path d="M1 2.5 L5 5.6 L9 2.5" fill="none" stroke="currentColor" stroke-width="1.1"/></symbol>
    <symbol id="icon-web" viewBox="0 0 10 10"><circle cx="5" cy="5" r="4" fill="none" stroke="currentColor" stroke-width="1.1"/><path d="M1 5 H9 M5 1 Q7.5 5 5 9 Q2.5 5 5 1" fill="none" stroke="currentColor" stroke-width="0.9"/></symbol>
  </defs>
</svg>

<!-- Letterhead -->
<section class="piece letterhead">
  <div class="side-band"></div>
  <div class="mark-dot"></div>
  <div class="brand-name">Pellmark Ridgeway LLC</div>
  <div class="tagline">Construction Consulting Services</div>
  <address class="sender">
    <div>2748 Fenwick Rd</div>
    <div>Maple Glen, NY 10943</div>
    <div class="gap"></div>
    <div>555 014 3627<svg class="icon"><use href="#icon-phone"/></svg></div>
    <div>p.lund@pellmarkridgeway.example<svg class="icon"><use href="#icon-mail"/></svg></div>
    <div>www.pellmarkridgeway.example<svg class="icon"><use href="#icon-web"/></svg></div>
  </address>
  <p class="greeting">Hello Elias,</p>
  <div class="body-copy">
    <p>Thank you for meeting with us last week. We have reviewed your site plans and project schedule, and we are pleased to outline how our team can support your crew through the coming season with planning, budgeting and hands-on field guidance.</p>
    <p>Our first step is a short review of your current workflow, equipment and staffing. From there we prepare a clear report with practical changes, cost estimates and a timeline that fits your budget. Each recommendation is explained in plain terms so your managers can act on it right away. We also meet with your foremen on site to confirm every detail before work begins, and we stay in touch by phone as the plan moves forward.</p>
    <p class="spaced">Technical training sessions can be held at your yard or on the job, for small groups or full crews. Sessions cover safety, scheduling, estimating and quality control, and can run for a few days or over several weeks.</p>
    <p>We travel across the country, so we can reach you wherever your next project takes you. Our rates include travel within the region, all course materials and a follow-up visit after training ends. If your needs change during the project, we will adjust the scope with you and update the estimate in writing. Please review the attached proposal and let us know which services you would like to begin with this spring.</p>
    <p class="spaced">We look forward to working with you and your team. Feel free to call or write with any questions about this letter.</p>
  </div>
  <p class="closing">Regards,</p>
  <p class="signer">Peter Lund</p>
  <div class="sign-rule"></div>
  <div class="signature" role="img" aria-label="Handwritten signature"></div>
  <div class="faint-mark"></div>
</section>

<!-- Presentation folder -->
<section class="piece folder">
  <div class="faint-mark"></div>
</section>

<!-- Business card, front -->
<section class="piece card-front">
  <div class="side-band"></div>
  <div class="mark-dot"></div>
  <div class="brand-name">Pellmark Ridgeway LLC</div>
  <div class="tagline">Construction Consulting Services</div>
  <ul class="services">
    <li>Business Consulting</li><li>Capital Investments</li><br><li>Marketing Implementations</li><li>Technical Training</li>
  </ul>
  <div class="person">Peter Lund</div>
  <div class="role">Director</div>
  <div class="rule"></div>
  <div class="contacts">
    <div><svg class="icon"><use href="#icon-phone"/></svg>555 014 3627</div>
    <div><svg class="icon"><use href="#icon-mail"/></svg>p.lund@pellmarkridgeway.example</div>
    <div><svg class="icon"><use href="#icon-web"/></svg>www.pellmarkridgeway.example</div>
  </div>
  <address class="address">
    <div>2748 Fenwick Rd</div>
    <div>Maple Glen, NY 10943</div>
  </address>
</section>

<!-- Business card, back (orange) -->
<section class="piece card-back is-orange">
  <div class="faint-mark"></div>
  <div class="brand-name">Pellmark Ridgeway LLC</div>
  <div class="web">www.pellmarkridgeway.example</div>
</section>

<!-- Envelope with flap -->
<section class="piece envelope">
  <div class="flap"></div>
  <div class="mark-dot"></div>
  <div class="brand-name">Pellmark Ridgeway LLC</div>
</section>

<!-- DL envelope -->
<section class="piece dl-envelope">
  <div class="side-band"></div>
  <div class="faint-mark"></div>
  <div class="brand-name">Pellmark Ridgeway LLC</div>
  <div class="contacts">
    <div><svg class="icon"><use href="#icon-phone"/></svg>555 014 3627</div>
    <div><svg class="icon"><use href="#icon-mail"/></svg>p.lund@pellmarkridgeway.example</div>
    <div><svg class="icon"><use href="#icon-web"/></svg>www.pellmarkridgeway.example</div>
  </div>
  <address class="address">
    <div>2748 Fenwick Rd</div>
    <div>Maple Glen, NY 10943</div>
  </address>
</section>

<!-- Business card, back (black) -->
<section class="piece card-back is-black">
  <div class="faint-mark"></div>
  <div class="brand-name">Pellmark Ridgeway LLC</div>
  <div class="web">www.pellmarkridgeway.example</div>
</section>

</body>
</html>
```